Software engineering company needs business card

I need a cool business card. Company: Soft Belan Brindlewood Ave 41 58207 Sincity Name: Gerald Vanholt CEO / Managing Director & Owner

```html
<!DOCTYPE html>
<html lang="en">
<head>
<meta charset="utf-8">
<title>Soft Belan – Business Card</title>
<link href="https://fonts.googleapis.com/css2?family=PT+Sans:wght@400;700&display=swap" rel="stylesheet">
<style>
  :root {
    --backdrop: #5a4a3c;
    --paper: #ffffff;
    --slate: #4e5053;
    --lime: #8bd11e;
    --ink: #5b5d60;
    --rule: #c9c9c9;
    --light: #ffffff;
  }
  * { margin: 0; padding: 0; box-sizing: border-box; }
  html, body {
    width: 1200px; height: 987px; overflow: hidden;
    background: var(--backdrop);
    font-family: "PT Sans", sans-serif;
  }
  .stage { position: relative; width: 1200px; height: 987px; }

  .card {
    position: absolute; left: 293px; width: 615px; height: 351px;
    overflow: hidden;
  }
  .card--front { top: 130px; background: var(--paper); }
  .card--back { top: 506px; background: var(--slate); }

  .brand-name {
    position: absolute;
    font-weight: 700;
    color: var(--lime);
    text-transform: uppercase;
    letter-spacing: 3px;
    white-space: nowrap;
  }
  .card--front .brand-name { left: 30px; top: 124px; font-size: 31px; }
  .card--back .brand-name {
    left: 0; right: 0; top: 150px; text-align: center; font-size: 50px; letter-spacing: 5px;
  }

  .divider {
    position: absolute; left: 312px; top: 54px; width: 1px; height: 206px;
    background: var(--rule);
  }

  .contact { position: absolute; left: 334px; top: 52px; color: var(--ink); }
  .contact__name { font-size: 23px; font-weight: 700; color: var(--lime); line-height: 28px; }
  .contact__role { font-size: 16px; line-height: 22px; }
  .contact__address { margin-top: 11px; font-size: 16px; line-height: 22px; }
  .contact__list { list-style: none; margin-top: 9px; }
  .contact__list li {
    display: flex; align-items: center; font-size: 16px; line-height: 23.5px;
  }
  .contact__list svg { width: 14px; height: 14px; margin-right: 9px; fill: var(--lime); flex: none; }

  .band { position: absolute; left: 0; top: 303px; width: 100%; height: 32px; background: var(--slate); }
  .band__lime { position: absolute; left: 0; top: 0; width: 475px; height: 100%; background: var(--lime); }

  .web {
    position: absolute; color: var(--light); letter-spacing: 3.5px; white-space: nowrap;
  }
  .band .web { left: 140px; top: 6px; font-size: 16px; }
  .card--back .web { left: 0; right: 0; top: 288px; text-align: center; font-size: 16px; }
</style>
</head>
<body>
<main class="stage">

  <section class="card card--front">
    <div class="brand-name">Soft Belan</div>
    <div class="divider"></div>
    <div class="contact">
      <div class="contact__name">Gerald Vanholt</div>
      <div class="contact__role">CEO / Geschäftsführer &amp; Inhaber</div>
      <div class="contact__address">Brindlewood Ave 41<br>Sincity 58207</div>
      <ul class="contact__list">
        <li><svg viewBox="0 0 16 16" aria-hidden="true"><path d="M3.5 1l3 3-1.6 2c.9 1.9 2.3 3.3 4.2 4.2l2-1.6 3 3-1.8 2.4C7 14 2 9 1.1 2.8z"/></svg>555 210 4871</li>
        <li><svg viewBox="0 0 16 16" aria-hidden="true"><path d="M4 0h8a1 1 0 0 1 1 1v14a1 1 0 0 1-1 1H4a1 1 0 0 1-1-1V1a1 1 0 0 1 1-1zm1 2v10h6V2zm3 11a1 1 0 1 0 0 2 1 1 0 0 0 0-2z"/></svg>555 390 7162</li>
        <li><svg viewBox="0 0 16 16" aria-hidden="true"><path d="M4 1h8v4H4zM1 6h14v6h-2v3H3v-3H1zm4 4v3h6v-3z"/></svg>555 764 0293</li>
        <li><svg viewBox="0 0 16 16" aria-hidden="true"><path d="M1 3h14v10H1zm1.5 1.5L8 9l5.5-4.5z"/></svg>name@softbelan.com</li>
      </ul>
    </div>
    <div class="band">
      <div class="band__lime"></div>
      <div class="web">www.softbelan.com</div>
    </div>
  </section>

  <section class="card card--back">
    <div class="brand-name">Soft Belan</div>
    <div class="web">www.softbelan.com</div>
  </section>

</main>
</body>
</html>
```